Business Card Design

we are a brand new cable TV network devoted to self improvement and leading a better life called FLOURIVO TV.I have a logo. We have 3 executives that need cards.I want it to be a heavy stock card: professional but showing our creative nature

Industry/Entity Type

Business

Contact Information for Business Card

CLAUDIA SAENZ AMLIECEO350 San Juan DrPonte Vedra Beach FL 32082904-473-5953

```html
<!DOCTYPE html>
<html lang="en">
<head>
<meta charset="utf-8">
<title>FLOURIVO TV — Business Card</title>
<link rel="stylesheet" href="https://fonts.googleapis.com/css2?family=Lato:wght@300;400;700;900&display=swap">
<style>
  :root {
    --backdrop: #1b1b1d;
    --card-white: #ffffff;
    --band-grey: #f2f2f2;
    --charcoal: #27282c;
    --ink: #1f2024;
    --accent-red: #c0272d;
    --rule-dark: #1a1b2a;
    --divider: #5a5c62;
    --text-light: #e9e9ea;
  }
  html, body {
    margin: 0;
    width: 1200px;
    height: 800px;
    overflow: hidden;
    background: var(--backdrop);
    font-family: "Lato", Arial, sans-serif;
  }
  .card {
    position: absolute;
    left: 180px;
    top: 160px;
    width: 840px;
    height: 480px;
    background: var(--card-white);
    overflow: hidden;
  }
  .top-band {
    position: absolute;
    left: 0; top: 0;
    width: 100%;
    height: 190px;
    background: var(--band-grey);
  }
  .top-band-extension {
    position: absolute;
    left: 0; top: 190px;
    width: 450px;
    height: 80px;
    background: var(--band-grey);
  }
  .band-rule {
    position: absolute;
    left: 450px; top: 188px;
    width: 390px;
    height: 4px;
    background: var(--rule-dark);
  }
  .contact-panel {
    position: absolute;
    left: 0; top: 270px;
    width: 450px;
    height: 210px;
    background: var(--charcoal);
  }
  .holder {
    position: absolute;
    left: 90px; top: 204px;
  }
  .holder-name {
    margin: 0;
    font-size: 21px;
    font-weight: 900;
    letter-spacing: 0.3px;
    line-height: 1.2;
    color: var(--ink);
    white-space: nowrap;
  }
  .holder-title {
    margin: 2px 0 0;
    font-size: 17px;
    font-weight: 400;
    line-height: 1.2;
    color: var(--accent-red);
  }
  .icon-tile {
    position: absolute;
    width: 64px;
    height: 40px;
    background: var(--accent-red);
    display: flex;
    align-items: center;
    justify-content: center;
  }
  .icon-tile svg { width: 22px; height: 22px; fill: var(--card-white); }
  .icon-tile.address { left: 322px; top: 270px; }
  .icon-tile.phone { left: 386px; top: 312px; }
  .contact-lines {
    position: absolute;
    left: 130px; top: 296px;
    width: 200px;
    color: var(--text-light);
    font-size: 17px;
    font-weight: 300;
    line-height: 1.3;
  }
  .contact-lines p { margin: 0; white-space: nowrap; }
  .contact-lines .divider {
    height: 1px;
    background: var(--divider);
    margin: 12px 0;
    width: 260px;
  }
  .contact-lines .phone-number { padding-left: 40px; }
  .brand {
    position: absolute;
    left: 540px; top: 318px;
    display: flex;
    align-items: center;
    gap: 12px;
    white-space: nowrap;
  }
  .brand-mark {
    width: 24px;
    height: 24px;
    background: var(--accent-red);
    flex: none;
  }
  .brand-name {
    font-size: 38px;
    font-weight: 900;
    color: var(--ink);
    letter-spacing: 0.5px;
    line-height: 1;
  }
</style>
</head>
<body>
  <section class="card" aria-label="FLOURIVO TV business card">
    <div class="top-band"></div>
    <div class="top-band-extension"></div>
    <div class="band-rule"></div>
    <div class="contact-panel"></div>

    <div class="holder">
      <h1 class="holder-name">MIRELLA OKAFOR DUNST</h1>
      <p class="holder-title">CEO</p>
    </div>

    <div class="icon-tile address" aria-label="Address">
      <svg viewBox="0 0 24 24"><path d="M12 3 2 12h3v8h5v-5h4v5h5v-8h3z"/></svg>
    </div>
    <div class="icon-tile phone" aria-label="Phone">
      <svg viewBox="0 0 24 24"><path d="M3 9c0-2 4-4 9-4s9 2 9 4v2h-5V9c-1-.6-2.5-1-4-1s-3 .4-4 1v2H3z"/><path d="M6 13h12l2 7H4z"/></svg>
    </div>

    <div class="contact-lines">
      <p>718 Harlow Creek Dr</p>
      <p>Calder Point Beach</p>
      <p>ME 04962</p>
      <div class="divider"></div>
      <p class="phone-number">555-618-2047</p>
      <div class="divider"></div>
    </div>

    <div class="brand">
      <span class="brand-mark"></span>
      <span class="brand-name">FLOURIVO TV</span>
    </div>
  </section>
</body>
</html>
```